Zielgruppe
Hausverwaltungen, Hausbesitzer.
Aufgabenstellung
Ergebnis soll ein Winword-Dokument mit einem Firmenlogo (Vorschlag: Tintenklecks hellgrün/blau verlaufend mit orangem Besen/Wischer/oder Hand - andere Ideen sind willkommen!) sein, das ich noch um Firmenname/Adresse bzw. Empfängerdaten noch vervollständigen/individualisieren kann. Es soll bunt, aber nicht überladen sein, eventuell mit Stockfotos von lachenden/glücklich schauenden aktiven Menschen sein, jung dynamisch aber nicht flippig. Folgender Text sollte darin vorkommen, Umformulierungen und andere Ideen sind hochwillkommen:
Unser Ziel ist es eine Hausbetreuung fast wie ein Hausbesorger zu leisten, jedoch mit zusätzlichen Vorteilen:
· Der Vertrag ist jederzeit ohne Frist kündbar, ohne Angabe von Gründen!
· Reinigung 1 x pro Woche sowie zusätzliche Bedarfsreinigung
· Krankheits- und Urlaubsvertretung sind bereits inklusive.
· Haftpflichtversicherung über 1,5 Mio. Euro
· Inklusive Gartenbetreuung, Garage, Dachboden, Haustechnik
· Kontrollgänge, 7 x 24 h Erreichbarkeit für Mieter und Eigentümer, Handwerkerüberwachung, Notfallkoordination
· Winterbetreuung der Gehsteige täglich mindestens zwischen 6:00 und 22:00
· Inklusive aller Hilfsmittel und Materialien
· Fixpreis pro Monat.
Nach Möglichkeit soll das auf 1 A4-Seite Platz finden.

```html
<!DOCTYPE html>
<html lang="de">
<head>
<meta charset="utf-8">
<title>Hausbetreuung Lutz Wendel</title>
<link rel="stylesheet" href="https://fonts.googleapis.com/css2?family=Merriweather:ital,wght@0,700;1,700&family=Open+Sans:wght@600&display=swap">
<style>
  :root {
    --bg-top: #d2d2d2;
    --bg-bottom: #b3b3b3;
    --ink: #555555;
    --white: #ffffff;
    --orange: #f26a1b;
  }
  * { margin: 0; padding: 0; box-sizing: border-box; }
  html, body { width: 848px; height: 1200px; overflow: hidden; }
  body { background: var(--bg-bottom); }
  .flyer {
    position: relative;
    width: 848px;
    height: 1200px;
    overflow: hidden;
    background: linear-gradient(180deg, var(--bg-top) 0%, #c4c4c4 45%, var(--bg-bottom) 100%);
  }
  .brand {
    position: absolute;
    left: 150px;
    top: 92px;
    display: flex;
    align-items: center;
    gap: 56px;
  }
  .brand-dot {
    width: 110px;
    height: 110px;
    border-radius: 50%;
    background: var(--white);
    flex: none;
  }
  .brand-name {
    font-family: "Open Sans", sans-serif;
    font-weight: 600;
    color: var(--ink);
    line-height: 1.1;
  }
  .brand-name .line-top { display: block; font-size: 30px; letter-spacing: 1px; }
  .brand-name .line-main { display: block; font-size: 52px; letter-spacing: 12px; }
  .stair-photo {
    position: absolute;
    left: 500px;
    top: 286px;
  }
  .promise {
    position: absolute;
    left: -20px;
    top: 362px;
    width: 640px;
    height: 96px;
    background: var(--orange);
    border-radius: 0 48px 48px 0;
    transform: rotate(-5deg);
    transform-origin: left center;
    display: flex;
    align-items: center;
    padding-left: 46px;
    padding-right: 40px;
  }
  .promise p {
    font-family: "Merriweather", serif;
    font-style: italic;
    font-weight: 700;
    font-size: 19px;
    line-height: 1.45;
    color: var(--white);
  }
  .benefits {
    position: absolute;
    left: 42px;
    top: 528px;
    list-style: none;
    font-family: "Merriweather", serif;
    font-weight: 700;
    font-size: 19px;
    line-height: 31px;
    color: var(--white);
    text-shadow: 0 1px 2px rgba(0,0,0,0.25);
  }
  .benefits li {
    position: relative;
    padding-left: 39px;
  }
  .benefits li::before {
    content: "·";
    position: absolute;
    left: 0;
    top: 0;
  }
  .contact {
    position: absolute;
    left: 0;
    right: 0;
    top: 1126px;
    text-align: center;
    font-family: "Open Sans", sans-serif;
    font-weight: 600;
    font-size: 19px;
    color: var(--ink);
  }
  .footer-bar {
    position: absolute;
    left: 203px;
    top: 1164px;
    width: 446px;
    height: 50px;
    background: var(--orange);
    border-radius: 10px 10px 0 0;
  }
</style>
</head>
<body>
<main class="flyer">
  <header class="brand">
    <span class="brand-dot"></span>
    <h1 class="brand-name">
      <span class="line-top">Hausbetreuung</span>
      <span class="line-main">Lutz Wendel</span>
    </h1>
  </header>

  <svg class="stair-photo" width="420" height="600" viewBox="0 0 420 600" role="img" aria-label="Foto einer hellen Treppe mit Edelstahl-Handlauf in einem Wohnhaus">
    <defs>
      <linearGradient id="stairTone" x1="0" y1="0" x2="1" y2="1">
        <stop offset="0" stop-color="#f4ece2"/>
        <stop offset="0.55" stop-color="#ddccb8"/>
        <stop offset="1" stop-color="#b7a58f"/>
      </linearGradient>
    </defs>
    <ellipse cx="240" cy="295" rx="230" ry="280" fill="#ffffff"/>
    <ellipse cx="255" cy="290" rx="192" ry="238" fill="url(#stairTone)"/>
  </svg>

  <div class="promise">
    <p>Unser Ziel ist es eine Hausbetreuung wie ein Hausbe-<br>sorger zu leisten, jedoch mit zusätzlichen Vorteilen:</p>
  </div>

  <ul class="benefits">
    <li>Der Vertrag ist jederzeit ohne Frist kündbar,<br>ohne Angabe von Gründen!</li>
    <li>Reinigung 1 x pro Woche sowie zusätzliche<br>Bedarfsreinigung</li>
    <li>Krankheits- und Urlaubsvertretung sind<br>bereits inklusive.</li>
    <li>Haftpflichtversicherung über 1,5 Mio. Euro</li>
    <li>Inklusive Gartenbetreuung, Garage,<br>Dachboden, Haustechnik</li>
    <li>Kontrollgänge, 7 x 24 h Erreichbarkeit für<br>Mieter und Eigentümer, Handwerkerüber-<br>wachung, Notfallkoordination</li>
    <li>Winterbetreuung der Gehsteige täglich<br>mindestens zwischen 6:00 und 22:00 Uhr</li>
    <li>Inklusive aller Hilfsmittel und Materialien</li>
    <li>Fixpreis pro Monat.</li>
  </ul>

  <footer>
    <p class="contact">Glanzweg 7 | 99999 Putzdorf | Tel: 0987 65 43 21-0 | Fax: 0987 65 43 21-99</p>
    <div class="footer-bar"></div>
  </footer>
</main>
</body>
</html>
```